Business card design for new eCommerce site focusing on integrity and strong businsess tactics

We need a business card that will stand out and be memorable. Something with color that matches our company logo colors. Think high end version of Dealvine. There are 2 logos provided. The parent company is called Bright Harbor Ventures and we are presenting a new and very exciting eCommerce site called KeenTraders.example.

Target Market(s)

Our target markets are in the Activities, Food and Beverage, Health and Beauty

Industry/Entity Type

Marketing

Contact Information for Business Card

We have 4 members that need cards...I will provide all info to the winner of the design contest
Business Address is
48730 West 61st Avenue, Suite C204
Phoenix AZ 85917

Font styles to use
Serif
Sans Serif

Colors

Designer to choose colors to be used in the design.

Requirements
Must have
• The card must be memorable...should be unique in design but must exude integrity and be playful .
• I have provided several colors or our parent company...please feel free to use which ever
Nice to have
• I will leave this up to you. Feel free to use other images of your choosing that wraps around our client.....Activities, Dining, Health, Beauty
Should not have
• just dont be boring

```html
<!DOCTYPE html>
<html lang="en">
<head>
<meta charset="utf-8">
<title>Bright Harbor Ventures – Business Card</title>
<link rel="stylesheet" href="https://fonts.googleapis.com/css2?family=Roboto:wght@300;400;500;700&display=swap">
<style>
  :root {
    --navy: #111b44;
    --lime: #a5c93f;
    --white: #ffffff;
    --ink: #1a1a1a;
    --card-black: #0c0c0e;
    --backdrop: #d9d4cc;
  }
  * { margin: 0; padding: 0; box-sizing: border-box; }
  html, body { width: 900px; height: 1200px; overflow: hidden; }
  body {
    background: var(--backdrop);
    font-family: "Roboto", Arial, sans-serif;
    position: relative;
  }
  .card {
    position: absolute;
    left: 85px;
    width: 733px;
    height: 428px;
    border-radius: 22px;
    overflow: hidden;
    box-shadow: 0 8px 18px rgba(0,0,0,0.35);
  }
  .card-front { top: 135px; background: var(--white); }
  .card-back { top: 630px; background: var(--card-black); }

  .name-disc { position: absolute; left: 0; top: 0; }
  .holder { position: absolute; left: 46px; top: 50px; }
  .holder-name { font-size: 26px; font-weight: 500; color: var(--white); }
  .holder-title { font-size: 18px; font-weight: 500; color: var(--lime); margin-top: 4px; }

  .contact-list { position: absolute; left: 46px; top: 272px; list-style: none; }
  .contact-list li {
    display: flex; align-items: center; gap: 9px;
    font-size: 16px; font-weight: 500; color: var(--ink);
    height: 25.5px;
  }
  .contact-list svg { width: 18px; height: 18px; flex: none; }

  .brand-mark { position: absolute; left: 416px; top: 54px; }
  .brand-name {
    position: absolute; left: 318px; width: 400px; top: 268px;
    text-align: center; color: var(--lime); font-weight: 700;
    font-size: 34px; line-height: 1.12;
  }

  .address-band {
    position: absolute; left: 0; right: 0; top: 376px; height: 32px;
    background: var(--navy); color: var(--white);
    font-size: 16px; text-align: center; line-height: 32px;
  }
  .accent-band {
    position: absolute; left: 0; right: 0; top: 411px; height: 17px;
    background: var(--lime);
  }

  .site-lockup {
    position: absolute; left: 160px; top: 184px;
    display: flex; align-items: center; gap: 16px;
  }
  .site-dot { width: 40px; height: 40px; border-radius: 50%; background: var(--lime); flex: none; }
  .site-name { font-size: 40px; font-weight: 500; color: var(--lime); line-height: 1; }
</style>
</head>
<body>

<section class="card card-front">
  <svg class="name-disc" width="330" height="225" viewBox="0 0 330 225" aria-hidden="true">
    <circle cx="160" cy="52" r="166" fill="none" stroke="var(--navy)" stroke-width="4"/>
    <circle cx="160" cy="52" r="158" fill="var(--navy)"/>
  </svg>
  <div class="holder">
    <p class="holder-name">Daniel Whitford</p>
    <p class="holder-title">Managing Director</p>
  </div>

  <ul class="contact-list">
    <li>
      <svg viewBox="0 0 18 18" aria-hidden="true"><path d="M3 6c0-2 2-3 6-3s6 1 6 3v1h-3V5.5H6V7H3zM5 8h8l2 6H3z" fill="var(--lime)"/></svg>
      602.555.0148
    </li>
    <li>
      <svg viewBox="0 0 18 18" aria-hidden="true"><rect x="2" y="4" width="14" height="10" fill="var(--lime)"/><path d="M2 4l7 6 7-6" fill="none" stroke="var(--white)" stroke-width="1.3"/></svg>
      hello@keentraders.example
    </li>
    <li>
      <svg viewBox="0 0 18 18" aria-hidden="true"><circle cx="9" cy="9" r="7.5" fill="var(--lime)"/><path d="M1.5 9h15M9 1.5c3 3 3 12 0 15M9 1.5c-3 3-3 12 0 15" fill="none" stroke="var(--white)" stroke-width="1"/></svg>
      www.keentraders.example
    </li>
  </ul>

  <svg class="brand-mark" width="206" height="206" viewBox="0 0 206 206" aria-hidden="true">
    <circle cx="103" cy="103" r="101" fill="var(--lime)"/>
  </svg>
  <p class="brand-name">Bright Harbor<br>Ventures</p>

  <div class="address-band">48730 West 61st Avenue, Suite C204, Phoenix AZ 85917</div>
  <div class="accent-band"></div>
</section>

<section class="card card-back">
  <div class="site-lockup">
    <span class="site-dot"></span>
    <p class="site-name">KeenTraders.example</p>
  </div>
</section>

</body>
</html>
```